Need a sleek, professional business card design for a Web Development business

I need a unique business card designed for a web development company. It is also the parent company for any ventures I do, such as my ClipWave channel, startup ideas I have, etc. I am the single member of "Bright Harbor Code LLC." I will attach my basic logo here, so you will see the current color scheme and have the asset available. Thank you!

Target Market(s)

Startups, SMB's, Professionals

Industry/Entity Type

Business

Font styles to use
Other font styles liked:
• Lovello for headings is what I use, but not necessary.

Colors

Designer to choose colors to be used in the design.

Requirements
Nice to have
• Sleek is the word. Professional, modern, dark.
Should not have
• Any work from someone else's design. Lacking originality.

```html
<!DOCTYPE html>
<html lang="en">
<head>
<meta charset="utf-8">
<title>Bright Harbor Code — Business Card</title>
<link href="https://fonts.googleapis.com/css2?family=Lato:wght@400;700&display=swap" rel="stylesheet">
<style>
  :root {
    --backdrop: #2b2b2b;
    --card: #000000;
    --coral: #ee6a73;
    --peach: #fd9f5e;
    --accent: #f58a5c;
    --ink: #ffffff;
  }
  * { margin: 0; padding: 0; box-sizing: border-box; }
  html, body { width: 1200px; height: 900px; overflow: hidden; }
  body {
    background: var(--backdrop);
    font-family: "Lato", sans-serif;
    color: var(--ink);
    position: relative;
  }
  .card {
    position: absolute;
    left: 250px;
    width: 700px;
    height: 400px;
    background: var(--card);
    overflow: hidden;
  }
  .card--back { top: 40px; }
  .card--front { top: 460px; }

  .brand-name {
    font-weight: 700;
    color: var(--accent);
    letter-spacing: 0.5px;
    display: flex;
    align-items: center;
    gap: 14px;
  }
  .brand-dot {
    width: 18px; height: 18px;
    border-radius: 50%;
    background: var(--accent);
  }
  .card--back .brand-name {
    position: absolute;
    top: 160px; left: 0; right: 0;
    justify-content: center;
    font-size: 42px;
  }
  .card--back .website {
    position: absolute;
    bottom: 44px; left: 0; right: 0;
    text-align: center;
    font-size: 20px;
    letter-spacing: 1px;
  }

  .card--front .brand-name {
    position: absolute;
    top: 92px; left: 44px;
    font-size: 30px;
    width: 250px;
    line-height: 1.15;
  }
  .divider {
    position: absolute;
    left: 330px; top: 60px;
    width: 2px; height: 180px;
    background: var(--accent);
  }
  .contact {
    position: absolute;
    left: 360px; top: 62px;
    font-size: 19px;
    line-height: 1.3;
  }
  .contact .person { font-size: 30px; font-weight: 700; color: var(--accent); line-height: 1.1; }
  .contact .role { font-size: 19px; margin-bottom: 10px; }
  .contact .address { margin-bottom: 8px; }
  .contact-line { display: flex; align-items: center; gap: 10px; }
  .contact-line svg { width: 16px; height: 16px; fill: var(--accent); flex: none; }

  .wave { position: absolute; left: 0; top: 0; width: 700px; height: 400px; }
  .card--front .website {
    position: absolute;
    left: 70px; top: 315px;
    font-size: 20px;
    letter-spacing: 1px;
    transform: rotate(14deg);
    transform-origin: left top;
  }
</style>
</head>
<body>

<section class="card card--back">
  <div class="brand-name"><span class="brand-dot"></span>Bright Harbor Code</div>
  <div class="website">www.brightharborcode.com</div>
</section>

<section class="card card--front">
  <svg class="wave" viewBox="0 0 700 400" aria-hidden="true">
    <defs>
      <linearGradient id="bandGradient" x1="0" y1="0" x2="1" y2="0">
        <stop offset="0" stop-color="#ee6a73"/>
        <stop offset="1" stop-color="#fd9f5e"/>
      </linearGradient>
    </defs>
    <path d="M0,236 C230,252 500,318 700,356 L700,400 L0,400 Z" fill="#ffffff"/>
    <path d="M0,250 C210,270 460,340 620,400 L0,400 Z" fill="url(#bandGradient)"/>
  </svg>

  <div class="brand-name"><span class="brand-dot"></span>Bright Harbor Code</div>
  <div class="divider"></div>

  <div class="contact">
    <div class="person">Daniel Reyes</div>
    <div class="role">Manager</div>
    <div class="address">418 Cedar Row<br>Austin, TX 78702</div>
    <div class="contact-line">
      <svg viewBox="0 0 16 16"><path d="M3 1h3l1.5 4-2 1.3a9 9 0 0 0 4.2 4.2L11 8.5l4 1.5v3a2 2 0 0 1-2 2A13 13 0 0 1 1 3a2 2 0 0 1 2-2z"/></svg>
      512 555 0142
    </div>
    <div class="contact-line">
      <svg viewBox="0 0 16 16"><path d="M4 1h8v4H4zM1 6h14v6h-3v3H4v-3H1zM5 10v3h6v-3z"/></svg>
      512 555 0143
    </div>
    <div class="contact-line">
      <svg viewBox="0 0 16 16"><path d="M1 3h14v10H1zM2 4.5v.4l6 4 6-4v-.4z"/></svg>
      info@brightharborcode.com
    </div>
  </div>

  <div class="website">www.brightharborcode.com</div>
</section>

</body>
</html>
```